EventVora Business Card

EventVora is a full-service meeting planning and management company specializing in turnkey corporate meetings and event planning. We focus on all the little details that make your event great so you don't have to worry about a thing. if you can visualize it, we can do it.

We are a small business - all women. We want our business cards to reflect our creative nature with a little touch of our spunky personality. We want to WOW from the start with these business cards.

website: www.eventvora-example.com

Contact Information for Business Card

I would like printing on front and back. back side should include our motto, "Always do what's expected, plus a little bit more!" and website with a design like attached. I would like the background color to be a blue that matches our logo. The front will probably need to be white and will need to include our logo and name, title and contact info. any additional design/color added would be nice as long as it flows with the design on the back of the card. I have attached two examples of other company's cards (dog walking & squish) as an example for the front.

```html
<!DOCTYPE html>
<html lang="en">
<head>
<meta charset="utf-8">
<title>EventVora Business Card</title>
<link rel="stylesheet" href="https://fonts.googleapis.com/css2?family=Montserrat:wght@400;700&family=Parisienne&family=Cinzel:wght@400&display=swap">
<style>
  :root {
    --page-bg: #ece8e2;
    --card-white: #ffffff;
    --brand-orange: #f47b20;
    --ornament-orange: #f79a52;
    --brand-blue: #1479b8;
    --ink: #1d1d1f;
    --on-orange: #ffffff;
  }
  * { box-sizing: border-box; margin: 0; padding: 0; }
  html, body {
    width: 1200px; height: 1076px; overflow: hidden;
    background: var(--page-bg);
  }
  .sheet {
    position: relative; width: 1200px; height: 1076px;
  }
  .card {
    position: absolute; left: 220px; width: 760px; height: 440px;
    border-radius: 22px; overflow: hidden;
    box-shadow: 0 4px 14px rgba(0,0,0,0.18);
  }

  /* Back side */
  .card-back { top: 60px; background: var(--brand-orange); color: var(--on-orange); }
  .ornament {
    position: absolute; left: 50%; transform: translateX(-50%);
    width: 150px; height: 64px; border-radius: 32px;
    background: var(--ornament-orange);
  }
  .ornament-top { top: 78px; }
  .ornament-bottom { top: 262px; }
  .motto {
    position: absolute; top: 168px; left: 0; width: 100%;
    text-align: center;
    font-family: "Parisienne", cursive; font-size: 42px; line-height: 1.4;
  }
  .back-web {
    position: absolute; bottom: 50px; left: 0; width: 100%;
    text-align: center;
    font-family: "Cinzel", serif; font-size: 14px; letter-spacing: 0.42em;
    text-transform: uppercase;
  }

  /* Front side */
  .card-front { top: 576px; background: var(--card-white); }
  .brand {
    position: absolute; left: 36px; top: 178px;
    display: flex; align-items: center; gap: 16px;
  }
  .brand-dot {
    width: 80px; height: 80px; border-radius: 50%;
    background: var(--brand-blue);
  }
  .brand-name {
    font-family: "Montserrat", sans-serif; font-weight: 400;
    font-size: 46px; color: var(--brand-blue); letter-spacing: -0.02em;
  }
  .divider {
    position: absolute; left: 391px; top: 100px; width: 2px; height: 222px;
    background: var(--brand-blue);
  }
  .contact {
    position: absolute; left: 424px; top: 104px;
    font-family: "Montserrat", sans-serif; color: var(--ink);
  }
  .person-name {
    font-weight: 700; font-size: 25px; color: var(--brand-blue);
    text-transform: uppercase; line-height: 1;
  }
  .person-title { font-size: 18px; line-height: 1.2; margin-top: 2px; }
  .address { font-size: 19px; line-height: 1.45; margin-top: 16px; }
  .lines { list-style: none; margin-top: 12px; }
  .lines li {
    display: flex; align-items: center; gap: 10px;
    font-size: 19px; line-height: 1.5;
  }
  .icon { width: 22px; height: 22px; flex: none; }
</style>
</head>
<body>
<main class="sheet">

  <section class="card card-back" aria-label="Card back">
    <div class="ornament ornament-top" role="img" aria-label="Decorative script flourish"></div>
    <p class="motto">Always do what’s expected, plus a little bit more!</p>
    <div class="ornament ornament-bottom" role="img" aria-label="Decorative script flourish"></div>
    <p class="back-web">www.eventvora-example.com</p>
  </section>

  <section class="card card-front" aria-label="Card front">
    <div class="brand">
      <span class="brand-dot"></span>
      <span class="brand-name">EventVora</span>
    </div>
    <div class="divider"></div>
    <div class="contact">
      <p class="person-name">Dana Whitfield</p>
      <p class="person-title">Maneger</p>
      <p class="address">2480 Meadow Ridge Rd.<br>Garland, TX 75040</p>
      <ul class="lines">
        <li>
          <svg class="icon" viewBox="0 0 22 22" aria-hidden="true">
            <rect width="22" height="22" rx="3" fill="#1479b8"/>
            <path d="M7 5c1 0 2 2.5 2 3s-1 1-1 1.5 1.5 3.5 3.5 4.5c.5 0 1-1 1.5-1s3 1 3 2-1.5 2-2.5 2C9 17 5 11 5 7c0-1 1-2 2-2z" fill="#fff"/>
          </svg>
          555-014-2290
        </li>
        <li>
          <svg class="icon" viewBox="0 0 22 22" aria-hidden="true">
            <rect width="22" height="22" rx="3" fill="#1479b8"/>
            <rect x="4" y="6" width="14" height="10" fill="none" stroke="#fff" stroke-width="1.5"/>
            <path d="M4 6l7 6 7-6M4 16l5-5M18 16l-5-5" fill="none" stroke="#fff" stroke-width="1.3"/>
          </svg>
          hello@eventvora-example.com
        </li>
        <li>
          <svg class="icon" viewBox="0 0 22 22" aria-hidden="true">
            <rect width="22" height="22" rx="3" fill="#1479b8"/>
            <g fill="none" stroke="#fff" stroke-width="1.2">
              <circle cx="11" cy="11" r="7"/>
              <ellipse cx="11" cy="11" rx="3" ry="7"/>
              <path d="M4 11h14M5 7.5h12M5 14.5h12"/>
            </g>
          </svg>
          www.eventvora-example.com
        </li>
      </ul>
    </div>
  </section>

</main>
</body>
</html>
```